A Dedicated Thank You to my Dad

Proposed Dimensions: Approx. 20" x 30"

For Father's Day, I wrote a dedication to my Dad that encapsulates my gratitude for everything he does, and everything he is. His birthday is on August 3, but it is more important for me to transform this dedication into a meaningful and memorable gift than to meet any deadline. I would love an image that captures the relationship between a father and his son, accompanied by my words of thanks in some sort of font that is appropriate for the message (calligprahy? not sure about that).

I had actually posted the Thank You on Pixelmarrow as a public post, so anyone with an account can read it: https://www.pixelmarrow.example/photo.php?fbid=40872219360548813&set=a.318760942157.6650129.3908471&type=1&theater

Only the words starting with "Thank you ..." should be on the poster.

Target Market(s)

This is a personal gift for my Dad. He doesn't have the best of eyesight, so having the words in a really small font would not be particularly helpful. :-)

Requirements
Must have
• * Personable
* Warm
* Inviting
* Memorable
* Understated more favored over Loud
Should not have
• * An entire palette of colors
* Wacky colors or fonts

```html
<!DOCTYPE html>
<html lang="en">
<head>
<meta charset="utf-8">
<title>Father — Husband: A Thank You</title>
<link href="https://fonts.googleapis.com/css2?family=Oswald:wght@400&family=Pathway+Gothic+One&display=swap" rel="stylesheet">
<style>
  :root {
    --navy-deep: #272262;
    --navy-edge: #353069;
    --violet-mid: #534f86;
    --violet-soft: #7b78a4;
    --pale: #e4e3ea;
    --gap: #ffffff;
    --ink: #111111;
    --title: #ffffff;
  }
  html, body {
    margin: 0;
    padding: 0;
    width: 1200px;
    height: 1200px;
    overflow: hidden;
    background: var(--gap);
  }
  .poster {
    display: block;
    width: 1200px;
    height: 1200px;
  }
  .tile { stroke: var(--gap); stroke-width: 7; stroke-linejoin: miter; }
  .tile--deep { fill: var(--navy-deep); }
  .tile--mid { fill: var(--violet-mid); }
  .tile--soft { fill: var(--violet-soft); }
  .tile--pale { fill: var(--pale); }
  .backdrop { fill: var(--navy-edge); }
  .pale-seam { stroke: #f1f0f5; stroke-width: 4; fill: none; }
  .role-title {
    font-family: "Oswald", sans-serif;
    font-weight: 400;
    font-size: 148px;
    fill: var(--title);
    text-anchor: middle;
  }
  .dedication {
    font-family: "Pathway Gothic One", sans-serif;
    font-size: 34px;
    fill: var(--ink);
    text-anchor: middle;
  }
</style>
</head>
<body>
<svg class="poster" viewBox="0 0 1440 1440" xmlns="http://www.w3.org/2000/svg">
  <defs>
    <linearGradient id="photo-son-father" x1="0" y1="0" x2="1" y2="1">
      <stop offset="0" stop-color="#b9b2a4"/>
      <stop offset="0.5" stop-color="#6e6258"/>
      <stop offset="1" stop-color="#3d4a66"/>
    </linearGradient>
    <linearGradient id="photo-wife-husband" x1="0" y1="0" x2="1" y2="1">
      <stop offset="0" stop-color="#c7ae86"/>
      <stop offset="0.55" stop-color="#a6806a"/>
      <stop offset="1" stop-color="#5a4b44"/>
    </linearGradient>
  </defs>

  <rect class="backdrop" x="0" y="0" width="1440" height="1440"/>

  <!-- top row -->
  <polygon class="tile" fill="url(#photo-son-father)" role="img"
           aria-label="Photo of a smiling son with his arm around his father at a family gathering"
           points="-20,-20 500,-20 565,225 425,480 120,480 -20,260"/>
  <polygon class="tile tile--soft" points="500,-20 990,-20 870,225 565,225"/>
  <polygon class="tile tile--deep" points="565,225 870,225 1010,480 425,480"/>
  <polygon class="tile tile--mid" points="990,-20 1320,-20 1460,225 1320,480 1010,480 870,225"/>

  <!-- middle band -->
  <polygon class="tile tile--pale" points="120,483 1320,483 1440,740 1320,997 120,997 0,740"/>
  <polyline class="pale-seam" points="425,483 290,740 425,997"/>
  <polyline class="pale-seam" points="1010,483 1150,740 1010,997"/>

  <!-- bottom row -->
  <polygon class="tile tile--mid" points="120,1000 425,1000 565,1255 440,1460 120,1460 -20,1255"/>
  <polygon class="tile tile--deep" points="425,1000 1010,1000 870,1255 565,1255"/>
  <polygon class="tile tile--soft" points="565,1255 870,1255 950,1460 490,1460"/>
  <polygon class="tile" fill="url(#photo-wife-husband)" role="img"
           aria-label="Photo of a wife hugging her husband from behind at home"
           points="1010,1000 1320,1000 1460,1200 1460,1460 950,1460 870,1255"/>

  <!-- titles -->
  <text class="role-title" x="1152" y="283">FATHER</text>
  <text class="role-title" x="278" y="1300">HUSBAND</text>

  <!-- dedication -->
  <g class="dedication">
    <text x="720" y="556">Thank you for welcoming more people to stay with us than I can count.</text>
    <text x="720" y="594">Thank you for my dry sense of humor. I cherish it.</text>
    <text x="720" y="633">Thank you for never giving up on trying to convince me that imperfection is not a failure.</text>
    <text x="720" y="671">Thank you for teaching me to try to find the good in everyone.</text>
    <text x="720" y="710">Thank you for showing me that there is peace to be found in stillness and quiet.</text>
    <text x="720" y="748">Thank you for demonstrating the fun that can be had and the truths that can be gleaned from debate.</text>
    <text x="720" y="787">Thank you for accepting me for who I am, no matter who I love, and for helping me to accept myself.</text>
    <text x="720" y="825">Thank you for doing whatever you can to help whoever you can, whether friend, family or stranger.</text>
    <text x="720" y="864">Thank you for trusting me enough to let your guard down to let me know how you are truly doing.</text>
    <text x="720" y="902">Thank you for insisting, year after year, that time with you means more than any gift I could ever purchase.</text>
    <text x="720" y="941">That is one lesson, amongst so many, that I will pass down to our next generation.</text>
  </g>
</svg>
</body>
</html>
```